Clean and sophisticated website for Darulnoor

Darulnoor is a group of enthusiasts offering education, welfare, health and publications. The organization is going through a re branding phase and looking to design a new website for darulnoor.org. The current landing page will be replaced by the new website. Looking for a creative design that could be converted into a responsive wordpress theme and integrated on the website.

The new website will have all the content of the 4 different sites that are accessible from the landing page.

Target Market(s)

Donors, information seekers, and students.

Industry/Entity Type

Non-Profit

Number of Pages Required

5+ page

Font styles to use
Sans Serif

Requirements
Must have
• Sophisticated look.
• Multi lingual interface (English + Urdu)
• Great User experience and Easy Navigation
• SEO friendly
• Prominent sections for 4 main categories
• Responsive design
Nice to have
• banners
• Parallax
• Call to action buttons
• simple clean design
Should not have
• Dark Colors
• Busy portal style look
• Flash
• cluttered design

```html
<!DOCTYPE html>
<html lang="en">
<head>
<meta charset="utf-8">
<title>Darulnoor</title>
<link href="https://fonts.googleapis.com/css2?family=Roboto:wght@300;400;500&family=Noto+Naskh+Arabic&display=swap" rel="stylesheet">
<style>
:root{
  --blue:#1c74c6;
  --blue-dark:#175fa6;
  --tile:#1f78c8;
  --green:#3bb34b;
  --green-line:#4cbd5a;
  --cell-head:#ececec;
  --cell-val:#8fbde6;
  --text-grey:#7a7a7a;
  --white:#ffffff;
  --nav-active:#1660a8;
  --lang:#3bb34b;
}
*{box-sizing:border-box;margin:0;padding:0}
html,body{width:904px;height:1200px;overflow:hidden}
body{font-family:"Roboto",Arial,sans-serif;background:var(--green);position:relative}
.site{position:relative;width:904px;height:1200px;overflow:hidden}

.hero{position:absolute;left:0;top:0;width:904px;height:486px;
  background:linear-gradient(180deg,#3f86d6 0%,#79b4ea 38%,#c9d9df 62%,#d9cdb7 75%,#5e8c4a 90%,#3f7d36 100%)}
.hero-arrow{position:absolute;top:228;}
.arrow{position:absolute;top:226px;width:16px;height:22px}
.arrow.left{left:12px}.arrow.right{right:12px}

.topnav{position:absolute;left:0;top:0;width:904px;height:32px;background:var(--blue);display:flex;padding-left:53px}
.topnav a{color:var(--white);text-decoration:none;font-size:11.5px;height:32px;line-height:32px;padding:0 15px;border-right:1px solid rgba(255,255,255,.15)}
.topnav a.active{background:var(--nav-active)}
.lang{position:absolute;right:41px;top:0;height:32px;width:53px;background:var(--lang);color:var(--white);font-size:12px;display:flex;align-items:center;justify-content:center;gap:4px;font-family:"Noto Naskh Arabic",serif}

.brand{position:absolute;left:54px;top:46px;display:flex;align-items:center;gap:12px}
.brand-mark{width:50px;height:76px;border:2px solid #3a3a3a}
.brand-name{font-size:17px;letter-spacing:3px;color:#2a2a2a;font-weight:400}

.tiles{position:absolute;left:64px;top:418px;display:flex;gap:23px}
.tile{width:180px;height:177px;background:var(--tile);color:var(--white);padding:18px 16px}
.tile svg{display:block;height:38px}
.tile h2{font-size:16.5px;font-weight:500;margin:10px 0 9px;letter-spacing:.2px}
.tile ul{list-style:none}
.tile li{font-size:10.5px;line-height:16.8px;display:flex;align-items:center;gap:6px}
.dot{width:9px;height:9px;border-radius:50%;background:var(--white);flex:none;position:relative}
.dot::after{content:"";position:absolute;left:2px;top:2px;width:4px;height:4px;border-right:1.4px solid var(--tile);border-bottom:1.4px solid var(--tile)}

.dome{position:absolute;left:0;top:0}

.namaz{position:absolute;left:0;top:692px;width:904px;text-align:center}
.namaz h1{font-weight:300;font-size:36px;color:var(--blue);margin-top:72px}
.times{position:absolute;left:205px;top:828px;border-collapse:separate;border-spacing:2px 0;font-size:11px}
.times th{background:var(--cell-head);color:#555;font-weight:400;width:82px;height:24px}
.times td{background:var(--cell-val);color:#333;font-size:12px;height:25px;text-align:center;border-top:1px solid var(--white)}

.story{position:absolute;left:124px;top:912px;width:375px}
.story h3{font-weight:300;font-size:27px;color:var(--blue);display:flex;align-items:center;gap:9px}
.story-icon{width:31px;height:31px;border-radius:50%;background:var(--blue)}
.story p{font-size:11.3px;font-weight:300;color:var(--text-grey);line-height:16.8px;margin-top:12px}
.story p+p{margin-top:16px}
.more{display:flex;align-items:center;gap:5px;margin-top:5px;font-size:11.5px;color:var(--blue)}
.more .dot{background:var(--blue)}.more .dot::after{border-color:var(--white)}

.video{position:absolute;left:516px;top:917px;width:272px;height:174px;background:radial-gradient(circle at 55% 45%,#d9c49a 0%,#4a86c8 35%,#0d0d12 80%)}
.play{position:absolute;left:110px;top:65px;width:50px;height:36px;background:var(--white);border-radius:8px}
.play::after{content:"";position:absolute;left:20px;top:9px;border-left:15px solid #1a2c55;border-top:9px solid transparent;border-bottom:9px solid transparent}
.bar{position:absolute;left:12px;bottom:11px;width:248px;height:16px;background:var(--white)}
.bar i{position:absolute;left:16px;top:7px;width:208px;height:2px;background:#ccc}
.bar b{position:absolute;left:16px;top:7px;width:58px;height:2px;background:#e8602c}

.footer{position:absolute;left:77px;top:1152px;font-size:11px;font-weight:300;color:var(--white)}
.social{position:absolute;right:62px;top:1147px;display:flex;gap:6px}
.social span{width:23px;height:23px;border-radius:50%;background:var(--white)}
</style>
</head>
<body>
<div class="site">
  <div class="hero" role="img" aria-label="Photograph of a white mosque with minarets and palm trees under a blue sky"></div>
  <svg class="arrow left" viewBox="0 0 16 22"><path d="M12 2 L4 11 L12 20" fill="none" stroke="#ffffff" stroke-width="1.5"/></svg>
  <svg class="arrow right" viewBox="0 0 16 22"><path d="M4 2 L12 11 L4 20" fill="none" stroke="#ffffff" stroke-width="1.5"/></svg>

  <nav class="topnav">
    <a class="active" href="#">HOME</a><a href="#">ABOUT</a><a href="#">PUBLICATIONS</a><a href="#">WELFARE</a><a href="#">EDUCATION</a><a href="#">BAYANAT</a><a href="#">CONTACT</a>
  </nav>
  <div class="lang">
    <svg width="10" height="10" viewBox="0 0 10 10"><circle cx="5" cy="5" r="4" fill="none" stroke="#fff"/><path d="M1 5h8M5 1v8" stroke="#fff" stroke-width=".8"/></svg>اردو
  </div>

  <div class="brand">
    <div class="brand-mark"></div>
    <div class="brand-name">DARULNOOR</div>
  </div>

  <svg class="dome" width="904" height="1200" viewBox="0 0 904 1200">
    <path d="M459,620 C470,640 510,660 560,670 C610,680 612,705 606,725 C640,720 720,745 745,810 C820,830 870,880 872,960 C876,1040 862,1100 840,1132 L64,1132 C42,1100 30,1040 34,960 C36,880 90,830 172,810 C196,745 276,720 310,725 C304,705 306,680 356,670 C406,660 448,640 459,620 Z" fill="#ffffff"/>
    <path d="M474,700 a26,26 0 1 1 -36,0 a22,22 0 1 0 36,0 Z" fill="#3bb34b"/>
    <path d="M440,694 l2,5 5,0 -4,3 2,5 -5,-3 -4,3 1,-5 -4,-3 5,0 Z" fill="#3bb34b"/>
    <rect x="452" y="712" width="3" height="26" fill="#3bb34b"/>
  </svg>

  <div class="tiles">
    <section class="tile">
      <svg viewBox="0 0 40 40" width="40"><circle cx="12" cy="10" r="8" fill="#fff"/><path d="M17 16 L33 32" stroke="#fff" stroke-width="5" stroke-linecap="round"/></svg>
      <h2>BAYANAT</h2>
      <ul><li><span class="dot"></span>Latest Morning Dars</li><li><span class="dot"></span>Latest Tarbiati Majlis</li><li><span class="dot"></span>Ramzan Bayans</li><li><span class="dot"></span>Nazmain</li></ul>
    </section>
    <section class="tile">
      <svg viewBox="0 0 40 40" width="40"><rect x="2" y="10" width="34" height="26" rx="5" fill="#fff"/><rect x="13" y="5" width="12" height="6" fill="none" stroke="#fff" stroke-width="2"/><circle cx="19" cy="23" r="8" fill="#1f78c8"/><path d="M19 18v10M14 23h10" stroke="#fff" stroke-width="3"/></svg>
      <h2>WELFARE</h2>
      <ul><li><span class="dot"></span>Ambulance</li><li><span class="dot"></span>Medical Assistance</li><li><span class="dot"></span>Coffin Bus</li><li><span class="dot"></span>Natural Disaster Relief</li></ul>
    </section>
    <section class="tile">
      <svg viewBox="0 0 40 40" width="40"><path d="M2 8 L19 12 L19 36 L2 32 Z M21 12 L38 8 L38 32 L21 36 Z" fill="#fff"/></svg>
      <h2>PUBLICATIONS</h2>
      <ul><li><span class="dot"></span>Insight Magazine</li><li><span class="dot"></span>Fahm-e-Noor Magazine</li><li><span class="dot"></span>Lumina Magazine</li><li><span class="dot"></span>Majallatunnoor</li></ul>
    </section>
    <section class="tile">
      <svg viewBox="0 0 40 40" width="40"><path d="M8 2 L20 5 L32 2 L32 20 L20 23 L8 20 Z" fill="#fff"/><path d="M2 30 C10 24 20 26 24 28 L34 24 C38 24 38 28 34 30 L22 36 L2 36 Z" fill="#fff"/></svg>
      <h2>EDUCATION</h2>
      <ul><li><span class="dot"></span>Courses for Brothers</li><li><span class="dot"></span>Courses for Sisters</li><li><span class="dot"></span>Volunteer with us</li></ul>
    </section>
  </div>

  <div class="namaz"><h1>Namaz Timing</h1></div>
  <table class="times">
    <tr><th>FAJAR</th><th>ZAHUR</th><th>ASAR</th><th>MAGRIB</th><th>ISHA</th><th>JUMMA</th></tr>
    <tr><td>6:25</td><td>1:30</td><td>4:30</td><td>SUNSET</td><td>7:30</td><td>1:30</td></tr>
  </table>

  <article class="story">
    <h3><span class="story-icon"></span>Compassion in Action</h3>
    <p>Darulnoor Welfare Trust began its humble beginnings in December, 2010. It was one of those rare moments when Allah (SWT) brings together kindred souls to work towards a common goal after tragedy has struck.</p>
    <p>Similarly a group of like minded humanitarians from varying professional and social backgrounds, came together to lend a helping hand and Darulnoor Welfare Trust was formed</p>
    <div class="more"><span class="dot"></span>read more</div>
  </article>

  <div class="video" role="img" aria-label="Video still of a mosque minaret seen through a patterned screen">
    <div class="play"></div>
    <div class="bar"><i></i><b></b></div>
  </div>

  <div class="footer">© Copyright 2016 Darulnoor. All rights reserved. &nbsp;| &nbsp;Feedback</div>
  <div class="social" aria-label="Social links"><span></span><span></span><span></span><span></span></div>
</div>
</body>
</html>
```